Artistically challenged consultant needs a sexy business card.

I need a business card design for my consultancy business. I work primarily in the pacific on international development program focusing on tourism, economic empowerment and training. I would like to use a light blue/green to reference the pacific and also a simple design of a sprouting coconut (photo attached for reference) to reference growth and development.
The business card should have icons for email, phone, skype, ABN and linked in.

Industry/Entity Type

Business

```html
<!DOCTYPE html>
<html lang="en">
<head>
<meta charset="utf-8">
<title>Mara Ellwood Consulting – Business Card</title>
<link href="https://fonts.googleapis.com/css2?family=Quicksand:wght@400;500&display=swap" rel="stylesheet">
<style>
  :root {
    --backdrop: #e4e6e8;
    --card-paper: #fdfef5;
    --pacific-blue: #2c9ecb;
    --sprout-tint-light: #d7eef6;
    --sprout-tint-deep: #9fd3e8;
  }
  * { margin: 0; padding: 0; box-sizing: border-box; }
  html, body {
    width: 1200px;
    height: 1000px;
    overflow: hidden;
    background: var(--backdrop);
  }
  .business-card {
    position: absolute;
    left: 169px;
    top: 277px;
    width: 860px;
    height: 494px;
    background: var(--card-paper);
    font-family: 'Quicksand', sans-serif;
    color: var(--pacific-blue);
  }
  .sprout-illustration {
    position: absolute;
    left: 72px;
    top: 26px;
    width: 190px;
    height: 442px;
    border-radius: 90px 90px 80px 80px;
    background: linear-gradient(180deg, var(--sprout-tint-light) 0%, var(--sprout-tint-deep) 100%);
  }
  .company-name {
    position: absolute;
    left: 372px;
    top: 136px;
    font-size: 28px;
    font-weight: 400;
    letter-spacing: 0.3px;
    white-space: nowrap;
  }
  .contact-list {
    position: absolute;
    left: 372px;
    top: 265px;
    list-style: none;
  }
  .contact-item {
    display: flex;
    align-items: center;
    height: 33.5px;
    font-size: 24px;
    font-weight: 400;
    white-space: nowrap;
  }
  .contact-icon {
    width: 32px;
    display: flex;
    justify-content: center;
    align-items: center;
    flex-shrink: 0;
  }
  .contact-icon svg { fill: var(--pacific-blue); }
  .abn-label {
    font-family: 'Quicksand', sans-serif;
    font-size: 8px;
    font-weight: 500;
    letter-spacing: 0.5px;
  }
</style>
</head>
<body>
  <article class="business-card">
    <div class="sprout-illustration" role="img" aria-label="Line drawing of a sprouting coconut with two leaves"></div>

    <h1 class="company-name">Mara Ellwood Consulting</h1>

    <ul class="contact-list">
      <li class="contact-item">
        <span class="contact-icon">
          <svg width="10" height="14" viewBox="0 0 10 14" aria-hidden="true">
            <path d="M2 0.5 L4 0.5 L4.6 4 L3.2 5 C3.6 7 4.6 8.6 6 9.6 L7.4 8.8 L9.6 11 L8.4 13.2 C4 12.4 0.6 7 0.6 2 Z"/>
          </svg>
        </span>
        <span class="contact-text">+61 400 123 456</span>
      </li>
      <li class="contact-item">
        <span class="contact-icon">
          <svg width="16" height="11" viewBox="0 0 16 11" aria-hidden="true">
            <rect x="0" y="0" width="16" height="11" rx="1"/>
            <path d="M0.8 1 L8 6.5 L15.2 1" fill="none" stroke="#fdfef5" stroke-width="1.4"/>
          </svg>
        </span>
        <span class="contact-text">me@maraellwoodconsulting.com</span>
      </li>
      <li class="contact-item">
        <span class="contact-icon">
          <svg width="15" height="15" viewBox="0 0 15 15" aria-hidden="true">
            <circle cx="7.5" cy="7.5" r="7.5"/>
          </svg>
        </span>
        <span class="contact-text">maraellwood</span>
      </li>
      <li class="contact-item">
        <span class="contact-icon"><span class="abn-label">ABN</span></span>
        <span class="contact-text">12 345 678 901</span>
      </li>
    </ul>
  </article>
</body>
</html>
```